Trevolo Ad Banners for Car Buying Service

We offer a fast, safe way for car owners to sell their car. They load the car details on our site, we give them a cash offer. If interested, we visit them and conclude deal, same day payment.
I want subtle animated banners for our Trevolo Display ads. (Dimensions - 120x600 - 160x600 - 300x250 - 300x600 - 320 x 50 - 728x90)
We can discuss messaging. I will attach recent static banners we had designed - and an older HTML5 animated version.
I'm looking for something subtle, modern but with clear call to action.
Car owners, male and female - wanting an easy, no fuss way to sell their car for cash
Automotive

```html
<!DOCTYPE html>
<html lang="en">
<head>
<meta charset="utf-8">
<title>Trevolo Display – Car Buying Banner</title>
<link href="https://fonts.googleapis.com/css2?family=Exo+2:wght@300;700;800&display=swap" rel="stylesheet">
<style>
  :root {
    --ink: #0a0a0a;
    --brand-blue: #0a9fe0;
    --deep-blue: #0a7fb5;
    --paper: #ffffff;
    --paper-shade: #e9ecef;
    --frame: #c9ced4;
    --stage: #050505;
    --muted-blue: #5f8ca6;
    --caption-white: #ffffff;
  }
  html, body {
    margin: 0;
    padding: 0;
    width: 833px;
    height: 1200px;
    overflow: hidden;
    background: var(--stage);
  }
  .board {
    display: block;
    width: 833px;
    height: 1200px;
    font-family: "Exo 2", "Trebuchet MS", sans-serif;
  }
  .headline { font-weight: 800; }
  .ink { fill: var(--ink); }
  .blue { fill: url(#blueText); }
  .font-label {
    font-weight: 800;
    fill: var(--brand-blue);
  }
  .font-caption {
    font-weight: 300;
    fill: var(--muted-blue);
  }
  .feature-line {
    font-weight: 700;
    fill: var(--caption-white);
  }
  .feature-line .accent { fill: var(--brand-blue); }
  .brand-name {
    font-weight: 800;
    fill: var(--ink);
  }
</style>
</head>
<body>
<svg class="board" viewBox="0 0 833 1200" xmlns="http://www.w3.org/2000/svg">
  <defs>
    <radialGradient id="stageGlow" cx="0.5" cy="1" r="0.6">
      <stop offset="0" stop-color="#0b2a44"/>
      <stop offset="0.45" stop-color="#06101a"/>
      <stop offset="1" stop-color="#050505"/>
    </radialGradient>
    <linearGradient id="panelFill" x1="0" y1="0" x2="1" y2="0">
      <stop offset="0" stop-color="#e4e7ea"/>
      <stop offset="0.12" stop-color="#ffffff"/>
      <stop offset="0.9" stop-color="#ffffff"/>
      <stop offset="1" stop-color="#eceff2"/>
    </linearGradient>
    <linearGradient id="waveFill" x1="0" y1="0" x2="0" y2="1">
      <stop offset="0" stop-color="#1294cf"/>
      <stop offset="1" stop-color="#0677a8"/>
    </linearGradient>
    <linearGradient id="blueText" x1="0" y1="0" x2="0" y2="1">
      <stop offset="0" stop-color="#0aa4e6"/>
      <stop offset="1" stop-color="#0a78ad"/>
    </linearGradient>
    <linearGradient id="carTone" x1="0" y1="0" x2="1" y2="0">
      <stop offset="0" stop-color="#8d9196"/>
      <stop offset="0.3" stop-color="#e6e8ea"/>
      <stop offset="0.5" stop-color="#fafafa"/>
      <stop offset="0.7" stop-color="#e3e5e7"/>
      <stop offset="1" stop-color="#8a8e93"/>
    </linearGradient>
    <clipPath id="panelClip">
      <rect x="283" y="22" width="267" height="1000" rx="14"/>
    </clipPath>
  </defs>

  <rect class="stage" width="833" height="1200" fill="url(#stageGlow)"/>

  <!-- Banner panel -->
  <g class="banner">
    <rect class="banner-frame" x="280" y="20" width="273" height="1005" rx="16" fill="#d3d8dd"/>
    <rect class="banner-face" x="283" y="22" width="267" height="1000" rx="14" fill="url(#panelFill)"/>
    <g clip-path="url(#panelClip)">
      <path class="banner-wave" fill="url(#waveFill)"
        d="M553,232 C553,280 530,298 492,303 L410,322 C330,340 283,365 283,430 L283,560 C283,515 305,488 350,482 L465,458 C525,446 553,420 553,380 Z"/>
      <path class="banner-fold" fill="none" stroke="#d6dadf" stroke-width="3"
        d="M283,815 C285,870 330,885 420,900 C500,912 540,920 553,960"/>
    </g>

    <text class="headline ink" x="416" y="104" text-anchor="middle" font-size="48" textLength="120" lengthAdjust="spacingAndGlyphs">WE DO</text>
    <text class="headline blue" x="417" y="141" text-anchor="middle" font-size="50" textLength="118" lengthAdjust="spacingAndGlyphs">MORE</text>
    <rect class="headline-rule" x="361" y="148" width="111" height="3" fill="var(--deep-blue)"/>
    <text class="headline ink" x="416" y="196" text-anchor="middle" font-size="52" textLength="116" lengthAdjust="spacingAndGlyphs">HELP</text>
    <text class="headline blue" x="415" y="234" text-anchor="middle" font-size="47" textLength="115" lengthAdjust="spacingAndGlyphs">MORE</text>

    <rect class="car-visual" x="332" y="266" width="168" height="373" rx="70" fill="url(#carTone)"
      role="img" aria-label="Top-down view of a silver sedan"/>

    <text class="headline blue" x="416" y="702" text-anchor="middle" font-size="37" textLength="123" lengthAdjust="spacingAndGlyphs">AND WE</text>
    <text class="headline blue" x="417" y="741" text-anchor="middle" font-size="48" textLength="127" lengthAdjust="spacingAndGlyphs">WANT</text>
    <text class="headline ink" x="417" y="788" text-anchor="middle" font-size="48" textLength="121" lengthAdjust="spacingAndGlyphs">YOUR</text>
    <text class="headline ink" x="418" y="846" text-anchor="middle" font-size="66" textLength="120" lengthAdjust="spacingAndGlyphs">CAR</text>
    <text class="headline blue" x="416" y="885" text-anchor="middle" font-size="47" textLength="115" lengthAdjust="spacingAndGlyphs">MORE</text>

    <text class="brand-name" x="417" y="980" text-anchor="middle" font-size="30" textLength="190" lengthAdjust="spacingAndGlyphs">Drivecash.co.za</text>
  </g>

  <!-- Presentation captions -->
  <text class="font-label" x="418" y="1094" text-anchor="middle" font-size="64" textLength="410" lengthAdjust="spacingAndGlyphs">VECTA SANS STD</text>
  <text class="font-caption" x="418" y="1130" text-anchor="middle" font-size="30" textLength="138" lengthAdjust="spacingAndGlyphs">FONT NAME</text>
  <text class="feature-line" x="416" y="1172" text-anchor="middle" font-size="33" textLength="780" lengthAdjust="spacingAndGlyphs">BANNER HAS FULLY <tspan class="accent">EDITABLE TEXT L</tspan>AYERS AND <tspan class="accent">ANIMATABLE</tspan></text>
</svg>
</body>
</html>
```